Bellucari Wine label**

Hi, we need a design for a white, red and sparkling wine label. We are a small italian restaurant (Bellucari) and we want to release some wines under our personal brand. The restaurant has a rustic, italian provance style with with a slight modern, clean lines look. We would like a design that represent our mission to provide as authentic Italian food as we can, something that feels that it has been brought from the heart of Italy.
https://www.bellucaricafe.example/

```html
<!DOCTYPE html>
<html lang="en">
<head>
<meta charset="utf-8">
<title>Bellucari Wine Labels</title>
<link rel="stylesheet" href="https://fonts.googleapis.com/css2?family=Cinzel:wght@400;500&family=Cormorant+Garamond:wght@500&family=Italianno&display=swap">
<style>
  :root {
    --canvas: #ffffff;
    --paper: #f4f2ed;
    --orange: #e8a33d;
    --orange-rule: #f3c77f;
    --ribbon: #f1efe6;
    --ink: #2b2b2b;
    --teal: #2e8f97;
    --maroon: #8b2c4a;
    --gold: #c49a4a;
    --white: #ffffff;
  }
  * { box-sizing: border-box; margin: 0; padding: 0; }
  html, body { width: 1200px; height: 904px; overflow: hidden; background: var(--canvas); }
  .canvas { position: relative; width: 1200px; height: 904px; }

  .label { position: absolute; top: 309px; width: 202px; height: 325px; text-align: center; }
  .label--orange { left: 168px; background: var(--orange); }
  .label--art { left: 512px; background: var(--paper); }
  .label--estate { left: 856px; background: var(--paper); }

  .label__frame { position: absolute; inset: 6px; border: 1px solid var(--orange-rule); }

  .brand-name {
    position: absolute; left: 0; right: 0;
    font-family: "Cormorant Garamond", serif; font-weight: 500;
    color: var(--ink); letter-spacing: 3px; text-transform: lowercase;
  }

  .ribbon {
    position: absolute; left: -10px; top: 87px; width: 222px; height: 44px;
    background: var(--ribbon);
  }
  .ribbon .brand-name { top: 6px; font-size: 26px; }

  .tagline {
    position: absolute; left: 12px; right: 12px; top: 149px; height: 32px;
    border-top: 1px solid var(--white); border-bottom: 1px solid var(--white);
    font-family: "Cinzel", serif; font-size: 21px; line-height: 30px;
    color: var(--white); letter-spacing: 1px;
  }

  .artwork { position: absolute; }
  .artwork--strip {
    left: 18px; top: 188px; width: 166px; height: 66px;
    border: 2px solid var(--white);
    background: linear-gradient(90deg, #8e3fc9, #e0459a 35%, #f29bc1 55%, #3fc4c9 80%, #f2b23d);
  }
  .artwork--panel {
    left: 5px; top: 96px; width: 193px; height: 173px;
    background: linear-gradient(135deg, #e23b6d, #8c3fd1 35%, #f5a02c 60%, #3a3fbf 85%, #f07fb5);
  }
  .artwork--vineyard {
    left: 20px; top: 60px; width: 164px; height: 96px;
    background: linear-gradient(180deg, #e9e7e2, #b9b6ae 70%, #8f8c85);
  }

  .wine-type {
    position: absolute; left: 0; right: 0;
    font-family: "Cinzel", serif; font-size: 14px; letter-spacing: 1px; color: var(--teal);
  }
  .wine-word {
    position: absolute; left: 0; right: 0;
    font-family: "Italianno", cursive; font-size: 30px; line-height: 1; color: var(--maroon);
  }

  .label--orange .wine-type { top: 264px; }
  .label--orange .wine-word { top: 280px; }

  .label--art .brand-name { top: 36px; font-size: 24px; }
  .label--art .wine-type { top: 276px; }
  .label--art .wine-word { top: 291px; }

  .label--estate .brand-name { top: 26px; font-size: 15px; }
  .estate-title {
    position: absolute; left: 10px; right: 10px; top: 170px; height: 52px;
    border-top: 2px solid var(--gold); border-bottom: 2px solid var(--gold);
    font-family: "Cinzel", serif; font-size: 30px; line-height: 48px;
    color: var(--ink); letter-spacing: 1px;
  }
  .label--estate .wine-type { top: 241px; }
  .label--estate .wine-word { top: 256px; }
  .vintage {
    position: absolute; left: 0; right: 0; top: 295px;
    font-family: "Cinzel", serif; font-size: 15px; color: var(--teal); letter-spacing: 1px;
  }
</style>
</head>
<body>
<main class="canvas">
  <section class="label label--orange">
    <div class="label__frame"></div>
    <div class="ribbon"><p class="brand-name">Bellucari</p></div>
    <p class="tagline">REAL TASTE</p>
    <div class="artwork artwork--strip" role="img" aria-label="Three panels of colourful abstract modern art"></div>
    <p class="wine-type">ITALIAN FINE</p>
    <p class="wine-word">wine</p>
  </section>

  <section class="label label--art">
    <p class="brand-name">Bellucari</p>
    <div class="artwork artwork--panel" role="img" aria-label="Colourful abstract modern art composition"></div>
    <p class="wine-type">ITALIAN FINE</p>
    <p class="wine-word">wine</p>
  </section>

  <section class="label label--estate">
    <p class="brand-name">Bellucari</p>
    <div class="artwork artwork--vineyard" role="img" aria-label="Engraved illustration of a hillside villa above rows of vines"></div>
    <h1 class="estate-title">BELLUCARI</h1>
    <p class="wine-type">ITALIAN FINE</p>
    <p class="wine-word">wine</p>
    <p class="vintage">2020</p>
  </section>
</main>
</body>
</html>
```